Gestaltung Flyer & Infokärtchen für Tellerbund
Zielgruppe
Hungrige Personen im Geschäft/Firma (keine Privatpersonen zu Hause), welche Menüs bestellen wollen. Die Menüs dürfen nicht zuviel kosten, aber der Flyer darf deshalb auch nicht "billig" daher kommen. Im Gegenteil.
Aufgabenstellung
Tellerbund - Deine Food Community ist eine seite, die virtuelle Bestellgemeinschaften schafft und damit Lieferpauschalen und Mindestbestellmengen für den Einzelbesteller umgeht. Der Einzelbesteller kennt also seine "Mitbesteller" nicht. Zudem wird das Menü günstiger, je mehr Leute in seiner Community bestellen. Diese Mitbesteller sind andere Personen in der gleichen Firma oder direkte Nachbarfirmen. In jedem Fall geht es um Bestellung von warmen Menüs.
Enorm wichtig und absolut zentral bei dem Infoflyer A4 UND dem kleinen Infokärtchen (A6 gefaltet mit aussen hinten weiss, aussen vorne Hauptmessage mit Logo (seperater Wettbewerb) und Innen zentrale Messages mit Internetseite www.TBM.ch) ist:
1. Der zentrale Unterschied zu anderen Bestellsystemen. warum der Kunde bei uns bestellen soll. Aus 2 Gründen!
1. "Keine Lieferpauschale", "Keine Mindestbestellmenge", "Punkte sammeln". Keine Lieferpauschale und keine Mindestbestellmenge - auch wenn nur 1 Menü bestellt wird. Bei Jedem Kauf kann der Besteller Punkte sammeln und diese dann in gratis Menü umwandeln. Zudem sammelt auch die virtuelle Bestellgemeinschaft punkte. Bei Erreichen von xy Punkten wird in der Community Preise verlost.
2. Community Gedanke: Je mehr bestellt wird, desto günstiger wird der Preis - bis zu einem bestimmten Minimum. Bei ersten Besteller kostet also bspw. das Menü warm geliefert all inkl. 15 Euro; bis minimum 9 Euro. Es muss aber voraus bezahlt werden (diese info muss aber ncht unbedingt auch drauf).
Beispiele für den Community Gedanken wären:
- "Tellerbund - Deine Food Community - Je mehr bestellen, desto günstiger wird’s"
- "Tellerbund - Deine Food Community - Andere bestellen - Du profitierst"
- "Tellerbund - Deine Food Community - Du bist teil der Community - mehr Besteller - günstiger Preis" etc.
- oder man stellt dies bildlich dar zusammen bspw. mit text 1 (ich stelle mir bspw. vor, 1 männchen hoher Preis ($ oben auf berg) und..

```html
<!DOCTYPE html>
<html lang="de">
<head>
<meta charset="utf-8">
<title>Tellerbund – Flyer</title>
<link rel="stylesheet" href="https://fonts.googleapis.com/css2?family=Source+Sans+3:wght@400;600;700&family=Kalam:wght@700&display=swap">
<style>
  :root {
    --orange: #d9822b;
    --orange-dark: #c46f1c;
    --blue: #4a84c3;
    --panel-top: #d7e7f2;
    --panel-bottom: #ffffff;
    --bubble: #c9dcea;
    --napkin: #f3f3f0;
    --napkin-shade: #dcdcd8;
    --green-light: #d6e6a8;
    --green-dark: #a9c46a;
    --food-a: #f2dc8a;
    --food-b: #8fb35a;
    --cursor-line: #333333;
    --white: #ffffff;
    --page: #ffffff;
  }
  * { margin: 0; padding: 0; box-sizing: border-box; }
  html, body { width: 1200px; height: 1200px; overflow: hidden; background: var(--page); }

  .flyer {
    position: absolute; left: 202px; top: 55px; width: 770px; height: 1088px;
    background: var(--orange);
    box-shadow: 3px 4px 10px rgba(0,0,0,0.25);
    overflow: hidden;
    font-family: "Source Sans 3", "Myriad Pro", sans-serif;
  }
  .panel {
    position: absolute; left: 12px; top: 12px; right: 12px; bottom: 50px;
    border-radius: 14px 0 0 0;
    background: linear-gradient(180deg, var(--panel-top) 0%, #eef4f9 45%, var(--panel-bottom) 80%);
  }
  .bubble-field {
    position: absolute; left: 12px; top: 12px; width: 400px; height: 380px;
    border-radius: 14px 0 0 0;
    background: radial-gradient(ellipse at 40% 35%, rgba(201,220,234,0.8), rgba(201,220,234,0) 70%);
  }
  .napkin { position: absolute; left: 0; top: 0; width: 770px; height: 400px; }

  .brand {
    position: absolute; left: 505px; top: 102px;
    display: flex; align-items: center; gap: 10px;
  }
  .brand-dot { width: 28px; height: 28px; border-radius: 50%; background: var(--orange); }
  .brand-name { font-weight: 700; font-size: 36px; color: var(--orange-dark); }

  .headline { position: absolute; left: 55px; top: 340px; color: var(--blue); font-weight: 600; line-height: 1; }
  .headline .line { display: block; white-space: nowrap; }
  .headline .line + .line { margin-top: 4px; margin-left: 66px; }
  .headline .small { font-size: 38px; }
  .headline .big { font-size: 84px; }

  .benefits { position: absolute; left: 58px; top: 532px; list-style: none; }
  .benefits li {
    display: flex; align-items: center; gap: 14px; height: 53px;
    font-family: "Kalam", cursive; font-weight: 700; font-size: 25px; color: var(--orange-dark);
  }
  .benefits svg { width: 28px; height: 28px; }

  .cta {
    position: absolute; left: 102px; top: 727px; width: 239px; height: 55px;
    border-radius: 8px;
    background: linear-gradient(180deg, var(--green-light), var(--green-dark));
    box-shadow: 2px 3px 5px rgba(0,0,0,0.3);
    color: var(--white); font-size: 29px; font-weight: 600;
    display: flex; align-items: center; justify-content: center;
    text-shadow: 0 1px 2px rgba(0,0,0,0.35);
  }
  .cta-pointer { position: absolute; left: 328px; top: 764px; width: 36px; height: 48px; }

  .food-photo {
    position: absolute; left: 12px; top: 790px; width: 430px; height: 260px;
    border-radius: 50% 60% 0 0 / 40% 50% 0 0;
    background: radial-gradient(ellipse at 45% 45%, var(--food-a) 0%, #e8d9a0 35%, var(--food-b) 60%, #dfe7ec 85%);
  }
  .band { position: absolute; left: 0; top: 0; width: 770px; height: 1088px; }
  .cursor-swarm {
    position: absolute; left: 0; top: 0; width: 770px; height: 1088px;
    filter: drop-shadow(2px 2px 2px rgba(0,0,0,0.3));
  }
  .url {
    position: absolute; left: 55px; top: 1030px;
    color: var(--white); font-weight: 700; font-size: 29px;
  }
</style>
</head>
<body>
  <div class="flyer">
    <div class="panel"></div>
    <div class="bubble-field" role="img" aria-label="Schwebende Blasen mit Preisnachlass-Zeichen"></div>

    <svg class="napkin" viewBox="0 0 770 400" role="img" aria-label="Gefaltete Papierserviette">
      <polygon points="352,0 770,0 770,272 482,362" fill="var(--napkin-shade)"/>
      <polygon points="345,0 770,0 770,258 475,345" fill="var(--napkin)"/>
    </svg>

    <div class="brand">
      <span class="brand-dot"></span>
      <span class="brand-name">Tellerbund</span>
    </div>

    <h1 class="headline">
      <span class="line"><span class="small">Je </span><span class="big">mehr</span><span class="small"> bestellen,</span></span>
      <span class="line"><span class="small">desto </span><span class="big">günstiger</span><span class="small"> wird’s</span></span>
    </h1>

    <ul class="benefits">
      <li><svg viewBox="0 0 28 28"><path d="M4 13h5v12H4zM10 24h11c2 0 3-1 3-2l1-7c0-2-1-3-3-3h-6l1-5c0-2-1-3-2-3l-5 8z" fill="none" stroke="#555" stroke-width="2" stroke-linejoin="round"/></svg>Keine Mindestbestellung</li>
      <li><svg viewBox="0 0 28 28"><path d="M4 13h5v12H4zM10 24h11c2 0 3-1 3-2l1-7c0-2-1-3-3-3h-6l1-5c0-2-1-3-2-3l-5 8z" fill="none" stroke="#555" stroke-width="2" stroke-linejoin="round"/></svg>Keine Lieferpauschal</li>
      <li><svg viewBox="0 0 28 28"><path d="M4 13h5v12H4zM10 24h11c2 0 3-1 3-2l1-7c0-2-1-3-3-3h-6l1-5c0-2-1-3-2-3l-5 8z" fill="none" stroke="#555" stroke-width="2" stroke-linejoin="round"/></svg>Essen und Punkte sammeln</li>
    </ul>

    <div class="cta">jetzt sparen</div>
    <svg class="cta-pointer" viewBox="0 0 36 48">
      <path d="M3 3v36l9-8 6 14 7-3-6-13h12z" fill="var(--white)" stroke="var(--cursor-line)" stroke-width="2" stroke-linejoin="round"/>
    </svg>

    <div class="food-photo" role="img" aria-label="Teller mit Nudeln und Gemüse"></div>

    <svg class="band" viewBox="0 0 770 1088">
      <path d="M0 950 C 150 990, 300 1015, 440 1022 L 770 1015 L 770 1088 L 0 1088 Z" fill="var(--orange)"/>
    </svg>

    <svg class="cursor-swarm" viewBox="0 0 770 1088" aria-hidden="true">
      <defs>
        <symbol id="cursor" viewBox="0 0 36 48">
          <path d="M3 3v36l9-8 6 14 7-3-6-13h12z" fill="var(--white)" stroke="var(--cursor-line)" stroke-width="2" stroke-linejoin="round"/>
        </symbol>
      </defs>
      <g>
        <use href="#cursor" x="705" y="800" width="34" height="46"/>
        <use href="#cursor" x="480" y="845" width="34" height="46"/>
        <use href="#cursor" x="600" y="852" width="34" height="46"/>
        <use href="#cursor" x="720" y="860" width="34" height="46"/>
        <use href="#cursor" x="638" y="890" width="34" height="46"/>
        <use href="#cursor" x="540" y="905" width="34" height="46"/>
        <use href="#cursor" x="698" y="905" width="34" height="46"/>
        <use href="#cursor" x="593" y="927" width="34" height="46"/>
        <use href="#cursor" x="660" y="935" width="34" height="46"/>
        <use href="#cursor" x="503" y="942" width="34" height="46"/>
        <use href="#cursor" x="458" y="950" width="34" height="46"/>
        <use href="#cursor" x="555" y="965" width="34" height="46"/>
        <use href="#cursor" x="683" y="965" width="34" height="46"/>
        <use href="#cursor" x="615" y="980" width="34" height="46"/>
        <use href="#cursor" x="735" y="980" width="34" height="46"/>
        <use href="#cursor" x="503" y="995" width="34" height="46"/>
        <use href="#cursor" x="443" y="1002" width="34" height="46"/>
        <use href="#cursor" x="563" y="1010" width="34" height="46"/>
        <use href="#cursor" x="630" y="1017" width="34" height="46"/>
        <use href="#cursor" x="698" y="1017" width="34" height="46"/>
        <use href="#cursor" x="368" y="1025" width="34" height="46"/>
        <use href="#cursor" x="750" y="1032" width="34" height="46"/>
        <use href="#cursor" x="413" y="1047" width="34" height="46"/>
        <use href="#cursor" x="473" y="1047" width="34" height="46"/>
        <use href="#cursor" x="533" y="1055" width="34" height="46"/>
        <use href="#cursor" x="593" y="1055" width="34" height="46"/>
        <use href="#cursor" x="713" y="1055" width="34" height="46"/>
        <use href="#cursor" x="653" y="1062" width="34" height="46"/>
        <use href="#cursor" x="390" y="1077" width="34" height="46"/>
        <use href="#cursor" x="458" y="1077" width="34" height="46"/>
        <use href="#cursor" x="548" y="1082" width="34" height="46"/>
        <use href="#cursor" x="638" y="1082" width="34" height="46"/>
        <use href="#cursor" x="728" y="1082" width="34" height="46"/>
      </g>
    </svg>

    <div class="url">www.tellerbund.ch</div>
  </div>
</body>
</html>
```